ボトル容器(280mL入り・画像参照)のオモテ面のラベルデザインを依頼します。
「食器洗いを楽しく!」というコンセプトを、手肌と環境へのやさしさという要素を盛り込みながら、ラベルのデザインとして表現してください。
パラダイスを感じさせるような、明るく、楽しく、元気でウキウキ、ワクワクするような雰囲気と同時に、予定価格が280mL入で1,300円前後と通常の食器洗剤と比べて高価格帯なので、安っぽさを感じさせない高級感も考慮してください。
当商品は今後、香りのバリエーション展開を予定しているので、ラベルの一部の色を替えることで、複数の香りバリエーションに対応できるデザインを希望します。
ラベルサイズ:幅50mm×高さ75mm以上100mm以下

以下の要素を入れてください。
商品名:Fluvorne
商品名の読み:フルヴォーン
品名:台所用せっけん
香り:○○○の香り
メインキャッチコピー:食器洗いを楽しく!
サブキャッチコピー:手肌と環境を守る水せっけん
シンプル 複雑
単色 カラフル
暗い 明るい
日常 高級
遊び心 厳粛
未来的 伝統的
女性的 男性的
• 高解像度JPG (.jpg)
• イラストレーター形式 (.ai)
添付画像のボトルに貼られたラベルのサイズは幅50mm×高さ75mmです。

コンセプトを最もよく表現していただいた提案でした。

とてもレベルの高い提案ばかりで、たいへん感謝しております。ありがとうございました。

```html
<!DOCTYPE html>
<html lang="ja">
<head>
<meta charset="utf-8">
<title>Fluvorne 台所用せっけん ラベル</title>
<link rel="stylesheet" href="https://fonts.googleapis.com/css2?family=M+PLUS+Rounded+1c:wght@500;800;900&display=swap">
<style>
  :root {
    --stripe-pink: #eba8a3;
    --stripe-white: #fdf6f3;
    --cocoa: #4f3129;
    --cocoa-soft: #6b463b;
    --brand-red: #c9281f;
    --blush: #f8cdc4;
    --cream: #fff8f2;
  }
  html, body {
    margin: 0;
    padding: 0;
    overflow: hidden;
    background: #ffffff;
  }
  .label {
    position: relative;
    width: 804px;
    height: 1200px;
    overflow: hidden;
    background: repeating-linear-gradient(
      90deg,
      var(--stripe-pink) 0 32px,
      var(--stripe-white) 32px 64px
    );
    font-family: "M PLUS Rounded 1c", sans-serif;
  }
  .palm-art {
    position: absolute;
    left: 250px;
    top: 100px;
    width: 320px;
    height: 200px;
    border-radius: 50% 50% 12px 12px;
    background: radial-gradient(ellipse at 50% 40%, #6a443a 0%, var(--cocoa) 70%);
  }
  .brand-reading {
    position: absolute;
    left: 370px;
    top: 236px;
    margin: 0;
    font-size: 30px;
    font-weight: 800;
    color: var(--brand-red);
    letter-spacing: 2px;
  }
  .brand-name {
    position: absolute;
    left: 0;
    width: 804px;
    top: 262px;
    margin: 0;
    text-align: center;
    font-size: 132px;
    line-height: 1;
    font-weight: 900;
    color: var(--brand-red);
    letter-spacing: 1px;
  }
  .catch-badge {
    position: absolute;
    left: 112px;
    top: 392px;
    width: 580px;
    height: 250px;
  }
  .catch-main {
    font-size: 50px;
    font-weight: 800;
    fill: var(--blush);
    letter-spacing: 4px;
  }
  .catch-sub {
    font-size: 40px;
    font-weight: 800;
    fill: var(--cocoa);
    letter-spacing: 2px;
  }
  .scent-band {
    position: absolute;
    left: 0;
    top: 985px;
    width: 804px;
    height: 66px;
    background: var(--cocoa-soft);
    border-top: 4px solid var(--cocoa);
    border-bottom: 4px solid var(--cocoa);
    box-sizing: border-box;
    display: flex;
    align-items: center;
    justify-content: center;
    color: var(--cream);
    font-size: 38px;
    font-weight: 800;
    letter-spacing: 3px;
  }
  .product-type {
    position: absolute;
    left: 0;
    top: 1056px;
    width: 804px;
    height: 110px;
    background: var(--cream);
    display: flex;
    align-items: center;
    justify-content: center;
    margin: 0;
    color: var(--cocoa);
    font-size: 48px;
    font-weight: 800;
    letter-spacing: 4px;
  }
</style>
</head>
<body>
  <main class="label">
    <div class="palm-art" role="img" aria-label="ヤシの木のシルエットのイラスト"></div>

    <p class="brand-reading">フルヴォーン</p>
    <h1 class="brand-name">Fluvorne</h1>

    <svg class="catch-badge" viewBox="0 0 580 250" aria-label="食器洗いを楽しく 手肌と環境を守る水せっけん">
      <ellipse cx="290" cy="70" rx="286" ry="66" fill="var(--cocoa)" stroke="var(--blush)" stroke-width="4"/>
      <text class="catch-main" x="290" y="88" text-anchor="middle">食器洗いを楽しく</text>
      <path id="sub-arc" d="M 30 150 Q 290 250 550 150" fill="none"/>
      <text class="catch-sub" text-anchor="middle">
        <textPath href="#sub-arc" startOffset="50%">手肌と環境を守る水せっけん</textPath>
      </text>
    </svg>

    <div class="scent-band">○○○の香り</div>
    <p class="product-type">台所用せっけん</p>
  </main>
</body>
</html>
```